Website for Accounting firm for dental practices

We need a website for our accounting firm for Dentists. We want it to be three pages, a HOME, SERVICES, and CONTACT US page. The logo for the firm is attached. Also attached is the wording we are going to use in the website. We would like the colors to go with the logo (the color logo). We want this page to look professional when people come to the page.

Industry/Entity Type

Accounting

Coding

Coded - Design and coding required

Number of Pages Required

1 page

```html
<!DOCTYPE html>
<html lang="en">
<head>
<meta charset="utf-8">
<title>Brightline Dental – Accounting and Financial Services for Dentists</title>
<link rel="stylesheet" href="https://fonts.googleapis.com/css2?family=Open+Sans:wght@400;600;700&display=swap">
<style>
:root{
  --blue:#3a8fd6;
  --ink:#2b2b2b;
  --text:#555;
  --green:#7cb342;
  --rule:#cfcfcf;
  --white:#fff;
}
*{margin:0;padding:0;box-sizing:border-box}
html,body{width:1200px;height:2839px;overflow:hidden}
body{font-family:"Open Sans",Arial,sans-serif;color:var(--text);background:var(--white);position:relative}

/* header */
.site-header{position:absolute;left:0;top:0;width:1200px;height:84px;background:var(--white);box-shadow:0 1px 4px rgba(0,0,0,.12);z-index:2}
.brand{position:absolute;left:100px;top:16px;display:flex;align-items:center;gap:8px;font-weight:700;font-size:22px;line-height:24px;color:var(--blue)}
.brand-mark{width:14px;height:14px;background:var(--blue);border-radius:50%}
.main-nav a{position:absolute;top:34px;font-size:14px;color:var(--ink);text-decoration:none}

/* hero */
.hero{position:absolute;left:0;top:84px;width:1200px;height:478px;background:linear-gradient(90deg,#eef0f2 0%,#e6e8ea 40%,#cfd3d6 70%,#aab2b7 100%)}
.hero-photo{position:absolute;left:480px;top:0;width:720px;height:478px;background:radial-gradient(ellipse at 55% 40%,#e9d9cf 0%,#cdbfb6 40%,#a9b2b5 75%,#8f999d 100%)}
.hero-title{position:absolute;left:100px;top:152px;font-size:44px;font-weight:700;color:var(--blue);letter-spacing:.5px}
.hero-sub{position:absolute;left:100px;top:212px;font-size:22px;font-weight:700;color:var(--ink);line-height:34px}
.btn{position:absolute;left:100px;top:302px;width:153px;height:45px;background:var(--blue);color:var(--white);font-size:13px;font-weight:700;display:flex;align-items:center;justify-content:center;text-decoration:none;border-radius:2px}
.hero-prev{position:absolute;left:35px;top:215px;width:36px;height:36px;border-radius:50%;background:rgba(120,120,120,.55)}

/* intro */
.section-title{position:absolute;left:0;width:1200px;text-align:center;font-size:23px;font-weight:600;color:var(--ink)}
.section-sub{position:absolute;left:0;width:1200px;text-align:center;font-size:20px;font-weight:700;color:var(--blue)}
.intro p{position:absolute;left:120px;width:960px;text-align:center;font-size:11px;line-height:22px;color:var(--text)}

.block-heading{position:absolute;font-size:20px;font-weight:700;color:var(--blue);line-height:28px}
.check-list{list-style:none}
.check-list li{position:absolute;font-size:13px;font-weight:600;color:#444;line-height:20px;padding-left:24px}
.check-list li svg{position:absolute;left:0;top:3px}

.photo{position:absolute}
.photo-tablet{background:linear-gradient(135deg,#7ea3c4,#dfe9f2 50%,#3f6fa6)}
.photo-desk{background:linear-gradient(135deg,#4a4a4a,#9a9a9a 45%,#e7e7e7 75%,#cfcfcf)}

.body-copy{position:absolute;left:100px;width:1000px;font-size:11px;line-height:25px;color:var(--text)}
.divider{position:absolute;left:100px;top:1535px;width:1000px;height:1px;background:var(--rule)}

.feature-title{position:absolute;font-size:15px;font-weight:700;color:var(--ink)}
.feature-text{position:absolute;font-size:12px;line-height:26px;color:var(--text)}
.icon-art{position:absolute;border-radius:4px}
.icon-clock{background:linear-gradient(180deg,#efefef,#c9c9c9)}
.icon-money{background:linear-gradient(180deg,#a9c99a,#6f9a5c)}
.icon-shield{background:linear-gradient(180deg,#6f8fd8,#2a4aa6)}
.icon-control{background:linear-gradient(180deg,#6e7a86,#33393f)}

/* call to action */
.cta{position:absolute;left:0;top:2385px;width:600px;height:324px;background:var(--blue);color:var(--white)}
.cta h2{position:absolute;left:100px;top:56px;font-size:22px;font-weight:700}
.cta p{position:absolute;left:100px;top:104px;width:450px;font-size:11px;line-height:24.5px}
.cta .contact{position:absolute;left:100px;top:212px;width:480px;font-size:23px;line-height:29px}
.cta .contact small{font-size:11px}
.cta-photo{position:absolute;left:600px;top:2385px;width:600px;height:324px;background:linear-gradient(90deg,#c7d3dc 0%,#e5e9ec 40%,#d9c6b8 70%,#f1ece8 100%)}

/* footer */
.site-footer{position:absolute;left:0;top:2709px;width:1200px;height:130px;background:var(--white)}
.footer-brand{position:absolute;left:100px;top:36px;font-weight:700;font-size:20px;line-height:22px;color:var(--blue)}
.footer-nav{position:absolute;left:263px;top:42px;font-size:11.5px;color:var(--ink)}
.footer-nav span{margin:0 16px;color:#777}
.copyright{position:absolute;left:263px;top:70px;font-size:11.5px;color:#666}
.social-label{position:absolute;left:770px;top:56px;font-size:11px;color:#555}
.social{position:absolute;top:48px;width:32px;height:32px;border-radius:50%}
</style>
</head>
<body>

<header class="site-header">
  <div class="brand"><span class="brand-mark"></span><span>Brightline<br>Dental</span></div>
  <nav class="main-nav">
    <a href="#" style="left:685px">Home</a>
    <a href="#" style="left:791px">About Us</a>
    <a href="#" style="left:916px">Services</a>
    <a href="#" style="left:1035px">Contact us</a>
  </nav>
</header>

<section class="hero">
  <div class="hero-photo" role="img" aria-label="Dentist in mask and gloves examining a young patient in the dental chair"></div>
  <div class="hero-prev"><svg width="36" height="36" viewBox="0 0 36 36"><path d="M21 11l-7 7 7 7" fill="none" stroke="#fff" stroke-width="3"/></svg></div>
  <h1 class="hero-title">WE PROVIDES</h1>
  <p class="hero-sub">ACCOUNTING AND FINANCIAL SERVICES<br>TO DENTISTS</p>
  <a class="btn" href="#">CLICK HERE</a>
</section>

<section class="intro">
  <h2 class="section-title" style="top:628px">ACCOUNTING AND FINANCIAL SERVICES FOR DENTISTS</h2>
  <h3 class="section-sub" style="top:676px">EXPERIENCED CPAS AT YOUR FINGERTIPS</h3>
  <p style="top:716px">Your time is valuable; and so is your money. The experienced certified public accountants at ChairsideCFO are here to save you both. We specialize in helping dental practices throughout the nation with all of their accounting and bookkeeping needs.</p>
  <p style="top:790px">Our unique understanding of the dental industry and your business needs sets us apart from any other accounting and bookkeeping firm in the U.S. All of our CPAs have worked in the industry for several years, giving us the expertise we need to handle any accounting issues no matter the size of your practice.</p>
</section>

<section class="outsourcing">
  <div class="photo photo-tablet" style="left:100px;top:899px;width:347px;height:199px" role="img" aria-label="Hands using a tablet showing a blue bar chart"></div>
  <h3 class="block-heading" style="left:483px;top:908px">BY OUTSOURCING<br>YOUR ACCOUNTING TO US YOU WILL</h3>
  <ul class="check-list">
    <li style="left:483px;top:988px"><svg width="14" height="12"><path d="M1 6l4 4 8-9" fill="none" stroke="#7cb342" stroke-width="2.5"/></svg>Receive accurate financial data monthly</li>
    <li style="left:483px;top:1025px"><svg width="14" height="12"><path d="M1 6l4 4 8-9" fill="none" stroke="#7cb342" stroke-width="2.5"/></svg>Compare your practice to industry averages</li>
    <li style="left:483px;top:1063px"><svg width="14" height="12"><path d="M1 6l4 4 8-9" fill="none" stroke="#7cb342" stroke-width="2.5"/></svg>Improve your cash flow</li>
    <li style="left:843px;top:988px"><svg width="14" height="12"><path d="M1 6l4 4 8-9" fill="none" stroke="#7cb342" stroke-width="2.5"/></svg>Allow you time to grow your practice</li>
    <li style="left:843px;top:1027px;width:270px"><svg width="14" height="12"><path d="M1 6l4 4 8-9" fill="none" stroke="#7cb342" stroke-width="2.5"/></svg>Spend more time with family and the things you enjoy</li>
  </ul>
</section>

<section class="monthly">
  <h3 class="block-heading" style="left:100px;top:1192px">MONTHLY WE WILL DO THE FOLLOWING</h3>
  <ul class="check-list">
    <li style="left:100px;top:1245px"><svg width="14" height="12"><path d="M1 6l4 4 8-9" fill="none" stroke="#7cb342" stroke-width="2.5"/></svg>Enter your transactions</li>
    <li style="left:100px;top:1283px"><svg width="14" height="12"><path d="M1 6l4 4 8-9" fill="none" stroke="#7cb342" stroke-width="2.5"/></svg>Reconcile your bank account</li>
    <li style="left:100px;top:1321px"><svg width="14" height="12"><path d="M1 6l4 4 8-9" fill="none" stroke="#7cb342" stroke-width="2.5"/></svg>Generate an income statement</li>
    <li style="left:100px;top:1359px"><svg width="14" height="12"><path d="M1 6l4 4 8-9" fill="none" stroke="#7cb342" stroke-width="2.5"/></svg>Calculate your taxes</li>
    <li style="left:426px;top:1245px"><svg width="14" height="12"><path d="M1 6l4 4 8-9" fill="none" stroke="#7cb342" stroke-width="2.5"/></svg>Generate a balance sheet</li>
    <li style="left:426px;top:1283px"><svg width="14" height="12"><path d="M1 6l4 4 8-9" fill="none" stroke="#7cb342" stroke-width="2.5"/></svg>Provide unlimited consultations</li>
    <li style="left:426px;top:1321px"><svg width="14" height="12"><path d="M1 6l4 4 8-9" fill="none" stroke="#7cb342" stroke-width="2.5"/></svg>Pay your bills</li>
  </ul>
  <div class="photo photo-desk" style="left:755px;top:1183px;width:347px;height:197px" role="img" aria-label="Woman at a desk using a calculator beside a keyboard"></div>
  <p class="body-copy" style="top:1424px">Like all professionals, you have business goals. In order to reach those goals, careful management of your finances is crucial. Trying to do it all on your own or with inexperienced bookkeepers could be a costly mistake. We will work with your staff, consults and other advisors to make your day to day financial hassles stress free. As a team with your other advisors we will help guide your practice to financial success and help ease the hassle of being a business owner.</p>
  <div class="divider"></div>
</section>

<section class="features">
  <h3 class="section-sub" style="top:1580px">MONTHLY WE WILL DO THE FOLLOWING</h3>

  <div class="icon-art icon-clock" style="left:100px;top:1643px;width:97px;height:121px" role="img" aria-label="Alarm clock icon"></div>
  <h4 class="feature-title" style="left:238px;top:1658px">SAVE TIME</h4>
  <p class="feature-text" style="left:238px;top:1686px;width:862px">With everything you have to do to run your dental practice on a daily, weekly and monthly basis, the extra hours you need to manage your finances, create invoices and pay your bills may not be easy to come by. Using our remote bookkeeping services allows you to run your business without worrying about the extra stuff.</p>

  <h4 class="feature-title" style="left:100px;top:1834px">SAVE MONEY</h4>
  <p class="feature-text" style="left:100px;top:1866px;width:840px">Using a remote accounting firm is far more affordable than keeping one in-house. Working with ChairsideCFO makes it so you don't have to pay extra employment taxes, benefits, wages or insurance, while still getting the high quality service you need. Our virtual bookkeeping costs 25 percent less than using services at a large CPA firm, with even more savings compared to hiring an internal bookkeeper.</p>
  <div class="icon-art icon-money" style="left:971px;top:1851px;width:118px;height:110px" role="img" aria-label="Stack of banknotes icon"></div>

  <div class="icon-art icon-shield" style="left:100px;top:1991px;width:108px;height:129px" role="img" aria-label="Blue shield icon with a question mark"></div>
  <h4 class="feature-title" style="left:240px;top:2010px">COMPARABILITY</h4>
  <p class="feature-text" style="left:240px;top:2038px;width:860px">With everything you have to do to run your dental practice on a daily, weekly and monthly basis, the extra hours you need to manage your finances, create invoices and pay your bills may not be easy to come by. Using our remote bookkeeping services allows you to run your business without worrying about the extra stuff.</p>

  <h4 class="feature-title" style="left:100px;top:2186px">MAINTAIN CONFIDENTIALITY</h4>
  <p class="feature-text" style="left:100px;top:2216px;width:840px">Using a remote accounting firm is far more affordable than keeping one in-house. Working with ChairsideCFO makes it so you don't have to pay extra employment taxes, benefits, wages or insurance, while still getting the high quality service you need. Our virtual bookkeeping costs 25 percent less than using services at a large CPA firm, with even more savings compared to hiring an internal bookkeeper.</p>
  <div class="icon-art icon-control" style="left:971px;top:2181px;width:127px;height:132px" role="img" aria-label="Dark joystick controller icon"></div>
</section>

<section class="cta">
  <h2>CALL CHAIRSIDECFO TODAY</h2>
  <p>Stop working harder and start working smarter. If you're handling your own accounting and other financial management, you are wasting valuable time and potentially costing yourself money. ChairsideCFO is a Harlow Professional Services, LLC company focused on working with dental professionals.</p>
  <p class="contact">Contact us today at 888-555-0142 or info@chairsidecfo.com <small>to find out more about our services.</small></p>
</section>
<div class="cta-photo" role="img" aria-label="Smiling support agent wearing a headset, colleagues blurred behind"></div>

<footer class="site-footer">
  <div class="footer-brand">Brightline<br>Dental</div>
  <nav class="footer-nav">Home<span>/</span>About Us<span>/</span>Services<span>/</span>Contact us</nav>
  <p class="copyright">© 2015, Brightline Dental. All Rights Reserved.</p>
  <span class="social-label">Connect with our social network :</span>
  <span class="social" style="left:951px;background:#3b5998" aria-label="Social network link"></span>
  <span class="social" style="left:991px;background:#35a8dc" aria-label="Social network link"></span>
  <span class="social" style="left:1031px;background:#1f6f8f" aria-label="Social network link"></span>
  <span class="social" style="left:1069px;background:#d6212e" aria-label="Social network link"></span>
</footer>

</body>
</html>
```